Business Card Design Project

We are a distribution company providing goods to Latin America. We sell everything from Medical equipment, generic medicines, to carecliners. The logo that we use is attached. The logo can incorporate different colors other than black for versatility. The company name is Valdoria International Corporation and/or VIC. The card will be printed using 1 or more of the following: Silk mounted and/or embossed. So if the design ideas could be made to incorporate that technique or any other unique techniques, it would be great. The target market is dialysis centers/doctors.

Basic Info for card:
Marnie Dowsett
Purchasing Manager
555-317-4086 direct
555-241-7953 fax
marnie.dowsett@valdoriavic.example
www.valdoriavic.example

Target Market(s)

Latin America

Industry/Entity Type

Business

Requirements
Nice to have
• The Front of the card should have the basic contact information with company name/logo. The back of the card could incorporate

```html
<!DOCTYPE html>
<html lang="en">
<head>
<meta charset="utf-8">
<title>Valdoria International Corporation – Business Card</title>
<link rel="stylesheet" href="https://fonts.googleapis.com/css2?family=Open+Sans:wght@400;700&display=swap">
<style>
  :root {
    --backdrop: #e9e6e2;
    --metal-light: #e6e6e6;
    --metal-mid: #9a9a9a;
    --metal-dark: #2b2b2b;
    --brand-red: #e8282b;
    --text-light: #f4f4f4;
    --divider: rgba(255,255,255,0.55);
  }
  * { margin: 0; padding: 0; box-sizing: border-box; }
  html, body {
    width: 1200px; height: 381px; overflow: hidden;
    background: var(--backdrop);
    font-family: "Open Sans", Arial, sans-serif;
  }
  .stage { position: relative; width: 1200px; height: 381px; }
  .card {
    position: absolute; top: 38px; width: 560px; height: 314px;
    overflow: hidden;
    background:
      repeating-linear-gradient(90deg, rgba(255,255,255,0.06) 0 1px, rgba(0,0,0,0.05) 1px 3px, rgba(255,255,255,0.03) 3px 5px),
      linear-gradient(180deg, var(--metal-light) 0%, var(--metal-mid) 45%, var(--metal-dark) 100%);
    box-shadow: 0 2px 6px rgba(0,0,0,0.25);
  }
  .card--front { left: 32px; }
  .card--back { left: 610px; }

  .brand-name {
    position: absolute; color: var(--text-light);
    font-weight: 700; text-align: center; white-space: nowrap;
  }
  .card--front .brand-name { left: 20px; top: 138px; width: 250px; font-size: 30px; }
  .card--back .brand-name { left: 0; top: 120px; width: 560px; font-size: 34px; }

  .divider {
    position: absolute; left: 287px; top: 55px; width: 1px; height: 190px;
    background: var(--divider);
  }
  .contact { position: absolute; left: 303px; top: 80px; width: 250px; color: var(--text-light); }
  .contact__name { color: var(--brand-red); font-size: 17px; font-weight: 700; line-height: 22px; }
  .contact__role { font-size: 14px; line-height: 22px; margin-bottom: 17px; }
  .contact__list { list-style: none; font-size: 12.5px; line-height: 21px; }
  .contact__list li { display: flex; align-items: center; gap: 7px; white-space: nowrap; }
  .contact__list svg { width: 12px; height: 12px; flex: none; }

  .company {
    position: absolute; left: 0; width: 560px; text-align: center; color: var(--text-light);
  }
  .company__name { top: 222px; font-size: 15px; font-weight: 700; letter-spacing: 1px; }
  .company__web { top: 264px; font-size: 14px; letter-spacing: 3px; }
</style>
</head>
<body>
<div class="stage">
  <section class="card card--front">
    <div class="brand-name">Valdoria</div>
    <div class="divider"></div>
    <div class="contact">
      <div class="contact__name">Marnie Dowsett</div>
      <div class="contact__role">Purchasing Manager</div>
      <ul class="contact__list">
        <li><svg viewBox="0 0 12 12"><circle cx="6" cy="6" r="5.3" fill="none" stroke="#f4f4f4" stroke-width="1.2"/><path d="M4 3.3l1 1.6-.6.6c.4.9 1.1 1.6 2 2l.6-.6 1.6 1-.6 1.2C5.8 9 3 6.2 2.9 4z" fill="#f4f4f4"/></svg>555-317-4086</li>
        <li><svg viewBox="0 0 12 12"><rect x="3" y="1.5" width="6" height="3" fill="#f4f4f4"/><rect x="1" y="4.5" width="10" height="4.5" rx="1" fill="#f4f4f4"/><rect x="3" y="8" width="6" height="2.5" fill="#f4f4f4"/></svg>555-241-7953</li>
        <li><svg viewBox="0 0 12 12"><rect x="1" y="3" width="10" height="7" rx="1" fill="#f4f4f4"/><path d="M1.5 3.5L6 7l4.5-3.5" fill="none" stroke="#555" stroke-width="1"/></svg>marnie.dowsett@valdoriavic.example</li>
        <li><svg viewBox="0 0 12 12" fill="none" stroke="#f4f4f4" stroke-width="1"><circle cx="6" cy="6" r="5"/><ellipse cx="6" cy="6" rx="2.2" ry="5"/><path d="M1 6h10M2 3.5h8M2 8.5h8"/></svg>www.valdoriavic.example</li>
      </ul>
    </div>
  </section>

  <section class="card card--back">
    <div class="brand-name">Valdoria</div>
    <div class="company company__name">Valdoria International Corporation</div>
    <div class="company company__web">www.valdoriavic.example</div>
  </section>
</div>
</body>
</html>
```